Bright Tooth Dentistry Business Card

We need business cards for our dental office.
We are looking for a clean, elegant design

We provide dental services to children.
Our card needs to be appealing to referring dentists, parents and our team

Target Market(s)

referring dentists, parents and our team

Industry/Entity Type

Dental Clinic

Contact Information for Business Card

4816 Juniper Lane, Suite 240
Cedar Ridge Heights, PA 15237

412-837-2961 Voice
412-837-2962 fax
info@brighttoothdentalpa.com email
www.brighttoothdentalpa.com web

Font styles to use
Sans Serif

Requirements
Must have
• White background - clean, crisp, elegant, simple
• rounded corners
• different color palate - once we come up with design, we will replace the blue with orange, green,
Nice to have
• Follow our logo typeface and colors
• then we can replace color

```html
<!DOCTYPE html>
<html lang="en">
<head>
<meta charset="utf-8">
<title>Bright Tooth Dentistry – Business Card</title>
<link href="https://fonts.googleapis.com/css2?family=Poppins:wght@400;500;600&family=Roboto:wght@400&display=swap" rel="stylesheet">
<style>
  :root {
    --bg: #1f1f1f;
    --brand-blue: #00aeef;
    --white: #ffffff;
    --grey-top: #b4b5b7;
    --grey-bottom: #a6a7a9;
  }
  * { margin: 0; padding: 0; box-sizing: border-box; }
  html, body {
    width: 1200px; height: 1200px; overflow: hidden;
    background: var(--bg);
    font-family: "Poppins", Arial, sans-serif;
  }
  .canvas { position: relative; width: 1200px; height: 1200px; }
  .card {
    position: absolute; left: 160px;
    width: 800px; height: 457px;
    border-radius: 26px; overflow: hidden;
    transform: scale(1.1); transform-origin: top left;
  }
  .card--front { top: 58px; background: var(--white); }
  .card--back {
    top: 640px;
    background: linear-gradient(180deg, var(--grey-top), var(--grey-bottom));
  }
  .front-panel { position: absolute; inset: 0; width: 100%; height: 100%; }
  .contact { position: absolute; left: 37px; top: 74px; color: var(--white); }
  .contact__name { font-size: 29px; font-weight: 500; line-height: 1.1; letter-spacing: 0.2px; }
  .contact__title { font-size: 21px; font-weight: 500; line-height: 1.2; }
  .contact__block { font-size: 19px; font-weight: 400; line-height: 24.5px; margin-top: 36px; }
  .contact__block + .contact__block { margin-top: 34px; }
  .brand-name {
    position: absolute; left: 430px; right: 10px; top: 325px;
    text-align: center; color: var(--brand-blue);
    font-size: 27px; font-weight: 600; letter-spacing: -0.2px;
  }
  .back-brand {
    position: absolute; left: 0; right: 0; top: 200px;
    text-align: center; color: var(--white);
    font-size: 44px; font-weight: 500;
  }
  .back-url {
    position: absolute; left: 0; right: 0; top: 384px;
    text-align: center; color: var(--white);
    font-family: "Roboto", Arial, sans-serif;
    font-size: 18px; letter-spacing: 3.4px;
  }
</style>
</head>
<body>
<div class="canvas">
  <section class="card card--front">
    <svg class="front-panel" viewBox="0 0 800 457" preserveAspectRatio="none" aria-hidden="true">
      <defs>
        <linearGradient id="panelBlue" x1="0" y1="0" x2="0" y2="1">
          <stop offset="0" stop-color="#00b9f0"/>
          <stop offset="1" stop-color="#00acec"/>
        </linearGradient>
      </defs>
      <path d="M0 0 H424 C470 22 478 90 458 152 C432 232 372 320 376 392 C379 432 402 450 424 457 H0 Z" fill="url(#panelBlue)"/>
      <path d="M424 0 C470 22 478 90 458 152 C432 232 372 320 376 392 C379 432 402 450 424 457" fill="none" stroke="#ffffff" stroke-width="7"/>
      <path d="M428 0 C478 18 480 92 464 152 C440 232 380 320 384 392 C387 430 405 448 422 457" fill="none" stroke="var(--brand-blue)" stroke-width="5"/>
    </svg>
    <div class="contact">
      <div class="contact__name">Daniel Mercer</div>
      <div class="contact__title">Founder &amp; CEO</div>
      <div class="contact__block">
        4816 Juniper Lane<br>
        Suite 240, Cedar Ridge<br>
        Heights, PA 15237
      </div>
      <div class="contact__block">
        P. 412-837-2961<br>
        M. 412-837-2962<br>
        info@brighttoothdentalpa.com<br>
        www.brighttoothdentalpa.com
      </div>
    </div>
    <div class="brand-name">Bright Tooth Dentistry</div>
  </section>

  <section class="card card--back">
    <div class="back-brand">Bright Tooth Dentistry</div>
    <div class="back-url">www.brighttoothdentalpa.com</div>
  </section>
</div>
</body>
</html>
```